Award-winnning Estate Agent needs a premium version of their 'For Sale' board design

We need a premium option for our 'For Sale' board design. We have a standard board that is attached to this brief, but were are looking to have a premium design version that we will use when selling exclusive properties. Our company name is Harbour Lane Estates and the name for this is exclusive selection is: 'The Harbour Collection'. The design needs to work with our current brand, but have a distinctive PREMIUM feel to it. I have uploaded the barnd guidelines and also some of the exisisting logo variations. We do NOT need a new logo but feel free to play around with colours, fonts, sizes etc. for the sign.

Target Market(s)

Property buyers & house hunters

Industry/Entity Type

Real Estate - Residential Property

Font styles to use
Sans Serif

Requirements
Must have
• A premium fee, must be square design, must be easy to read when driving past the sign
Nice to have
• I'm open ot ideas

```html
<!DOCTYPE html>
<html lang="en">
<head>
<meta charset="utf-8">
<title>Harbour Lane Estates – For Sale Board</title>
<link rel="stylesheet" href="https://fonts.googleapis.com/css2?family=Arimo:wght@400;700&display=swap">
<style>
  :root {
    --navy: #2b3990;
    --mid-blue: #1777bc;
    --accent-blue: #0a72b8;
    --accent-soft: #cfe3f3;
    --white: #ffffff;
  }
  html, body {
    margin: 0;
    padding: 0;
    width: 1200px;
    height: 1200px;
    overflow: hidden;
    background: var(--white);
  }
  .board { display: block; width: 1200px; height: 1200px; }
  .board text { font-family: "Arimo", Arial, sans-serif; }
  .frame { fill: var(--white); stroke: var(--navy); stroke-width: 20; }
  .band-primary { fill: var(--navy); }
  .band-secondary { fill: var(--mid-blue); }
  .footer-band { fill: var(--navy); }
  .brand-square { fill: var(--mid-blue); }
  .accent-area { fill: url(#accentFade); }
  .collection-title { fill: var(--white); font-weight: 400; font-size: 134px; }
  .collection-subtitle { fill: var(--white); font-weight: 400; font-size: 112px; }
  .agent-name { fill: var(--navy); font-weight: 700; font-size: 100px; }
  .sale-label { fill: var(--navy); font-weight: 700; font-size: 278px; }
  .phone { fill: var(--accent-blue); font-weight: 700; font-size: 272px; }
  .website { fill: var(--white); font-weight: 400; font-size: 122px; }
</style>
</head>
<body>
<svg class="board" viewBox="0 0 1932 1932" xmlns="http://www.w3.org/2000/svg" role="img" aria-label="Harbour Lane Estates, The Harbour Collection, For Sale, 01632 960412, www.harbourlaneestates.co.uk">
  <defs>
    <linearGradient id="accentFade" x1="0" y1="0" x2="1" y2="0">
      <stop offset="0" stop-color="#cfe3f3"/>
      <stop offset="1" stop-color="#9cc6e6"/>
    </linearGradient>
  </defs>

  <rect class="frame" x="5" y="5" width="1922" height="1922"/>

  <!-- Collection banner -->
  <polygon class="band-primary" points="895,10 1922,10 1922,258 1020,258"/>
  <text class="collection-title" x="1866" y="193" text-anchor="end">The Harbour</text>
  <polygon class="band-secondary" points="1171,275 1922,275 1922,425 1247,425"/>
  <text class="collection-subtitle" x="1862" y="380" text-anchor="end">Collection</text>

  <!-- Agent identity -->
  <rect class="brand-square" x="402" y="83" width="305" height="305"/>
  <text class="agent-name" x="105" y="515" textLength="900" lengthAdjust="spacingAndGlyphs">Harbour Lane Estates</text>

  <!-- Sale message with accent areas -->
  <rect class="accent-area" x="651" y="560" width="808" height="150" rx="40" role="img" aria-label="Decorative speech mark accent, upper curve"/>
  <text class="sale-label" x="710" y="940" textLength="586" lengthAdjust="spacingAndGlyphs">FOR</text>
  <text class="sale-label" x="620" y="1188" textLength="740" lengthAdjust="spacingAndGlyphs">SALE</text>
  <rect class="accent-area" x="508" y="1225" width="807" height="251" rx="40" role="img" aria-label="Decorative speech mark accent, lower curve with pointer"/>

  <!-- Contact -->
  <text class="phone" x="175" y="1724" textLength="1602" lengthAdjust="spacingAndGlyphs">01632 960412</text>
  <rect class="footer-band" x="10" y="1774" width="1912" height="148"/>
  <text class="website" x="966" y="1880" text-anchor="middle" textLength="1570" lengthAdjust="spacingAndGlyphs">www.harbourlaneestates.co.uk</text>
</svg>
</body>
</html>
```